Retirement maintenance and reinstatment brochure

We are looking for a capability statement/brochure outlining our skills and capabilities for maintenance, reinstatement and refurbishment work specific to the requirements of retirement villages in Australia

We are a new company, however our people have significant experience working in this industry

Target Market(s)

Retirement living facilities, aged care facilities, hospitals

Industry/Entity Type

Building

Colors

Designer to choose colors to be used in the design.

Requirements
Must have
• Not alot of wording. Stock images of building refurbishment to retirement living and aged care (carpenters, painters etc)
Nice to have
• 1-2 pages only
Should not have
• alot of meaningless writing

```html
<!DOCTYPE html>
<html lang="en">
<head>
<meta charset="utf-8">
<title>Swift Reach Maintenance Services – Capability Brochure</title>
<link href="https://fonts.googleapis.com/css2?family=Oswald:wght@400;500;600&family=Roboto+Condensed:wght@300;400;700&display=swap" rel="stylesheet">
<style>
  :root{
    --navy:#0f3a6b;
    --navy-deep:#0b2d55;
    --red:#d01c2a;
    --sky:#8ccaf0;
    --white:#ffffff;
    --page:#ffffff;
  }
  html,body{margin:0;padding:0;width:1200px;height:1200px;overflow:hidden;background:var(--page);}
  .canvas{position:relative;width:1200px;height:1200px;}
  .abs{position:absolute;}

  /* left panel */
  .intro{left:16px;top:223px;width:582px;height:753px;background:var(--navy);overflow:hidden;}
  .intro-photo{left:0;top:240px;width:582px;height:513px;
    background:
      radial-gradient(ellipse 45% 40% at 12% 88%,rgba(12,24,40,.95) 0%,rgba(12,24,40,.6) 45%,rgba(12,24,40,0) 100%),
      radial-gradient(ellipse 70% 50% at 55% 55%,rgba(120,185,230,.55) 0%,rgba(120,185,230,0) 100%),
      linear-gradient(180deg,var(--navy) 0%,#2465a0 30%,#2f77b2 55%,#1f5a92 80%,#143e6e 100%);}
  .header-card{left:0;top:0;width:582px;height:135px;}
  .brand{left:150px;top:28px;display:flex;align-items:center;gap:14px;}
  .brand-dot{width:62px;height:62px;border-radius:50%;background:var(--navy);flex:none;}
  .brand-name{font-family:'Oswald',sans-serif;font-weight:500;color:var(--navy);line-height:1;}
  .brand-name .big{display:block;font-size:40px;letter-spacing:.3px;}
  .brand-name .small{display:block;font-size:12px;letter-spacing:2.4px;margin-top:4px;}

  .headline{left:0;top:157px;width:582px;margin:0;text-align:center;white-space:nowrap;
    font-family:'Oswald',sans-serif;font-weight:500;font-size:21px;line-height:26.4px;color:var(--white);
    text-transform:uppercase;transform:scaleX(.83);transform-origin:center top;}
  .response-box{left:41px;top:267px;width:145px;height:216px;background:var(--red);text-align:center;}
  .response-box p{margin:14px -20px 0;white-space:nowrap;font-family:'Oswald',sans-serif;font-weight:500;font-size:16.5px;line-height:21.8px;color:var(--white);text-transform:uppercase;transform:scaleX(.84);transform-origin:center top;}
  .response-box svg{display:block;margin:12px auto 0;}
  .expertise{left:207px;top:265px;margin:0;font-family:'Roboto Condensed',sans-serif;font-weight:300;font-size:16px;line-height:19.4px;color:var(--sky);}

  .bubble{border-radius:50%;border:3px solid var(--white);box-sizing:border-box;}

  /* photo column */
  .gallery{left:602px;top:223px;width:280px;height:753px;}
  .gallery div{position:absolute;left:0;width:280px;}

  /* right panel */
  .trades-panel{left:882px;top:223px;width:302px;height:753px;background:var(--navy);overflow:hidden;}
  .compliance{left:22px;top:40px;width:240px;margin:0;font-family:'Roboto Condensed',sans-serif;font-size:16px;line-height:19.4px;color:var(--white);text-align:justify;text-align-last:center;}
  .trades{right:40px;top:500px;margin:0;text-align:right;font-family:'Roboto Condensed',sans-serif;font-size:16px;line-height:19.4px;color:var(--white);}
  .trades strong{font-weight:700;}
  .toolbox{left:44px;top:603px;width:110px;height:100px;border-radius:4px;
    background:radial-gradient(ellipse at 40% 20%,#b9b9b9 0%,rgba(185,185,185,0) 45%),linear-gradient(170deg,#e8474f,#a8121c);}
</style>
</head>
<body>
<div class="canvas">

  <!-- Left panel -->
  <section class="abs intro">
    <div class="abs intro-photo" role="img" aria-label="Photo of a tradesperson's tool belt with screwdrivers and pliers in a renovation site"></div>

    <svg class="abs header-card" viewBox="0 0 582 135" aria-hidden="true">
      <polygon points="56,-3 528,-3 472,131 112,131" fill="#fff" stroke="#d01c2a" stroke-width="5"/>
    </svg>
    <div class="abs brand">
      <span class="brand-dot"></span>
      <span class="brand-name"><span class="big">SWIFT REACH</span><span class="small">MAINTENANCE SERVICES</span></span>
    </div>

    <h1 class="abs headline">Swift Reach Maintenance Services is a commercial building and<br>maintenance company established and located on the Sunshine<br>Coast in QLD.</h1>

    <div class="abs response-box">
      <p>We have the ability<br>to react quickly and<br>complete works<br>with as little as 24<br>hours notice.</p>
      <svg width="62" height="62" viewBox="0 0 64 64" fill="none" stroke="#fff" stroke-width="2.2" stroke-linecap="round">
        <circle cx="32" cy="34" r="22"/>
        <circle cx="32" cy="34" r="17"/>
        <path d="M12 16a8 8 0 0 1 12-6M52 16a8 8 0 0 0-12-6"/>
        <path d="M32 24v11l-7 6"/>
        <path d="M16 54l-4 5M48 54l4 5"/>
      </svg>
    </div>

    <p class="abs expertise">We have expertise in retirement living and aged care<br>maintenance works such as cleaning and painting<br>programs, reinstatement works including painting and<br>carpet replacement as well as<br>major refurbishment or<br>upgrade works<br>including kitchen and<br>bathroom works,<br>electrical and air<br>conditioning<br>upgrade works.</p>

    <div class="abs bubble" style="left:354px;top:355px;width:188px;height:188px;background:radial-gradient(ellipse 30% 45% at 60% 55%,#f4f4f6 0%,rgba(244,244,246,0) 100%),linear-gradient(100deg,#ece8de 0%,#e3dccd 60%,#c99a55 82%,#ddd5c4 100%);" role="img" aria-label="Photo of a painter on a ladder rolling paint onto a wall"></div>
    <div class="abs bubble" style="left:288px;top:523px;width:108px;height:108px;background:linear-gradient(180deg,#cfa89a 0%,#b98f7c 45%,#efeae2 70%,#8b6a4f 100%);" role="img" aria-label="Photo of a bathroom being stripped for renovation"></div>
    <div class="abs bubble" style="left:488px;top:541px;width:60px;height:60px;background:linear-gradient(135deg,#e9e2d0 0%,#e6c23a 50%,#d8453a 100%);" role="img" aria-label="Photo of an electrician testing with a multimeter"></div>
    <div class="abs bubble" style="left:398px;top:575px;width:100px;height:100px;background:linear-gradient(180deg,#4f9be0 0%,#3f86cc 55%,#2d5f8e 75%,#7a6250 100%);" role="img" aria-label="Photo of a roofer working on a roof"></div>
    <div class="abs bubble" style="left:184px;top:613px;width:72px;height:72px;background:linear-gradient(180deg,#6ea9dc 0%,#8aa6bf 40%,#8a6040 75%,#5a3c28 100%);" role="img" aria-label="Photo of a building under construction with scaffolding"></div>
    <div class="abs bubble" style="left:268px;top:635px;width:60px;height:60px;background:linear-gradient(160deg,#f2ebe0 0%,#e8ddcb 50%,#b58a5f 100%);" role="img" aria-label="Photo of a kitchen under refurbishment"></div>
  </section>

  <!-- Photo column -->
  <section class="abs gallery">
    <div style="top:0;height:187px;background:linear-gradient(180deg,#9fb7c9 0%,#5f7d4a 30%,#7a5a3a 58%,#5e8f3a 78%,#3f6a2c 100%);" role="img" aria-label="Photo of a cottage with a timber deck among trees"></div>
    <div style="top:189px;height:186px;background:linear-gradient(180deg,#f0eee8 0%,#e2ddd2 45%,#8e7a66 62%,#8a6238 100%);" role="img" aria-label="Photo of an open living room with fireplace and staircase"></div>
    <div style="top:377px;height:186px;background:linear-gradient(180deg,#f1efea 0%,#b88a5f 25%,#e6e2da 45%,#6e4a2e 70%,#8f6c4c 100%);" role="img" aria-label="Photo of a renovated kitchen with timber cabinets"></div>
    <div style="top:566px;height:187px;background:linear-gradient(180deg,#ece9e1 0%,#e3ddcf 50%,#a07c56 70%,#6e5236 100%);" role="img" aria-label="Photo of a bright living area with timber floors"></div>
  </section>

  <!-- Right panel -->
  <section class="abs trades-panel">
    <p class="abs compliance">We are licensed and insured, and have a full workplace health and safety compliance system.</p>
    <svg class="abs" style="left:0;top:0" width="302" height="753" viewBox="0 0 302 753">
      <defs>
        <linearGradient id="gearTone" x1="0" y1="0" x2="1" y2="1">
          <stop offset="0" stop-color="#f7f3ee"/>
          <stop offset=".3" stop-color="#f47a24"/>
          <stop offset=".7" stop-color="#ef5a14"/>
          <stop offset="1" stop-color="#f2b21c"/>
        </linearGradient>
      </defs>
      <polygon points="22,111 302,111 302,289 22,477" fill="url(#gearTone)" role="img" aria-label="Photo of an orange safety helmet with yellow ear muffs"/>
      <polygon points="22,505 302,317 302,753 22,753" fill="#d01c2a"/>
    </svg>
    <div class="abs toolbox" role="img" aria-label="Illustration of a red toolbox full of tools"></div>
    <p class="abs trades"><strong>Trades we specialise in:</strong><br>Painting and building cleaning<br>Carpentry and minor repairs<br>Plastering and rendering<br>Carpet and floor laying<br>Electrical<br>Plumbing<br>Air<br>conditioning<br>upgrades</p>
  </section>

</div>
</body>
</html>
```